Boutique Jewellery Card [UPDATED] Embossing and Foil

Hi Designers,

What will win you this competition is your input on making my card look very professional and classy

Just some overview information.

I am striving to be the most prestigious jeweller going around specialising in custom designed jewellery, engagement rings and repairs on a bigger budget.

I am spending a lot on the printing including thick cards, rounded corners, multi level embossing and foiling.

Front:

I want my entire logo on the front, which I will have embossed and foiled (source file included)
Optional: I also want a lower embossing of a repeating pattern which I am not sure on. I need YOUR input here

Back:

I need you to use your skills and experience to make my details look very important, professional and classy.

The details I need on the back are:

Marcus Delvaney
Your Jewellery Stylist

www.marcusdelvaney.com
0492 836 514
marcus@marcusdelvaney.com

The font MUST match the font/style used in the logo.
Everything else including layout, whether my logo is on the back etc, engrave/endent, foiling etc is what I need your input for
Updates

Project Deadline Extended Reason: I was a bit slow and out of action at the start, but we're almost there, just need a few more days to finalize Added Sunday, November 16, 2014

Target Market(s)

25 - 80 year olds. Fashion concious. Wealthy

Industry/Entity Type

Printing

Contact Information for Business Card

Marcus Delvaney
Your Jewellery Stylist

0492 836 514
marcus@marcusdelvaney.com
www.marcusdelvaney.com
- facebook and instagram logo's

Requirements
Must have
• Must use the font from my logo on the back, or very similar
• My logo on the front
• My details on the back must be the centre of attention, my logo can still be there but is less important.
• Back must include the facebook and instagram logo's
Nice to have
• repeating pattern or monogram

```html
<!DOCTYPE html>
<html lang="en">
<head>
<meta charset="utf-8">
<title>Marcus Delvaney – Business Card</title>
<link rel="stylesheet" href="https://fonts.googleapis.com/css2?family=Open+Sans:wght@300;400;700&family=Raleway:wght@400;500&display=swap">
<style>
  :root {
    --canvas-bg: #efefef;
    --card-white: #ffffff;
    --navy-deep: #000000;
    --navy-blue: #1f4f97;
    --silver: #c3c7ce;
    --silver-light: #e6e8ec;
    --silver-soft: #9ea4ae;
    --ink: #1a1a1a;
    --ink-muted: #5a5a5a;
    --rule: #9a9a9a;
  }
  * { margin: 0; padding: 0; box-sizing: border-box; }
  html, body {
    width: 1200px; height: 1000px; overflow: hidden;
    background: var(--canvas-bg);
  }
  .canvas { position: relative; width: 1200px; height: 1000px; }

  .card {
    position: absolute; top: 104px;
    width: 434px; height: 260px; overflow: hidden;
  }

  /* Front */
  .card--front {
    left: 144px;
    background:
      radial-gradient(ellipse 85% 95% at 12% 92%, var(--navy-blue) 0%, rgba(31,79,151,0.55) 40%, rgba(0,0,0,0) 78%),
      linear-gradient(225deg, var(--navy-deep) 0%, #050b1a 45%, #143872 100%);
    font-family: "Raleway", sans-serif;
    color: var(--silver);
    text-align: center;
  }
  .front-mark {
    position: absolute; left: 50%; top: 44px;
    width: 72px; height: 72px; margin-left: -36px;
    border: 9px solid var(--silver); border-radius: 50%;
  }
  .front-name {
    position: absolute; left: 0; right: 0; top: 128px;
    font-size: 17px; font-weight: 400; letter-spacing: 1.6px; line-height: 20px;
    text-transform: uppercase; color: var(--silver);
  }
  .front-tagline {
    position: absolute; left: 0; right: 0; top: 145px;
    font-size: 10.5px; font-weight: 500; letter-spacing: 3.4px; line-height: 12px;
    text-transform: uppercase; color: var(--silver-soft);
  }
  .front-country {
    position: absolute; left: 0; right: 0; top: 157px;
    font-size: 6.5px; font-weight: 500; letter-spacing: 3px; line-height: 8px;
    text-transform: uppercase; color: var(--silver-soft);
  }
  .front-ornament {
    position: absolute; left: 0; right: 0; top: 194px; height: 58px;
    background:
      radial-gradient(ellipse 50% 50% at 50% 60%, rgba(230,232,236,0.95) 0%, rgba(195,199,206,0.75) 45%, rgba(195,199,206,0) 100%),
      radial-gradient(ellipse 60% 32% at 50% 62%, rgba(195,199,206,0.55) 0%, rgba(195,199,206,0) 100%);
  }

  /* Back */
  .card--back {
    left: 621px;
    background: var(--card-white);
    font-family: "Open Sans", sans-serif;
    color: var(--ink);
  }
  .back-brand {
    position: absolute; left: 0; top: 68px; width: 190px;
    display: flex; flex-direction: column; align-items: center; gap: 8px;
  }
  .back-brand__circle {
    width: 44px; height: 44px; border: 7px solid var(--ink); border-radius: 50%;
  }
  .back-brand__name {
    font-size: 10px; font-weight: 400; letter-spacing: 0.6px;
    text-transform: uppercase; color: var(--ink);
  }
  .back-divider {
    position: absolute; left: 190px; top: 56px;
    width: 1px; height: 90px; background: var(--rule);
  }
  .back-identity { position: absolute; left: 224px; top: 53px; }
  .back-identity__name {
    font-size: 14px; font-weight: 400; letter-spacing: 0.1px;
    text-transform: uppercase; line-height: 18px;
  }
  .back-identity__role {
    font-size: 9.5px; font-weight: 300; color: var(--ink-muted); line-height: 12px;
  }
  .contact-list {
    position: absolute; left: 225px; top: 102px;
    list-style: none;
  }
  .contact-list__item {
    display: flex; align-items: center; gap: 7px;
    height: 15px; font-size: 9.5px; color: var(--ink);
  }
  .contact-list__icon { width: 11px; height: 11px; flex: none; }
  .back-shadow {
    position: absolute; left: 66px; top: 180px; width: 302px; height: 8px;
    background: radial-gradient(ellipse 50% 100% at 50% 0%, rgba(0,0,0,0.22) 0%, rgba(0,0,0,0) 100%);
  }
  .back-country {
    position: absolute; left: 0; right: 0; top: 200px;
    text-align: center; font-size: 9px; font-weight: 700;
    letter-spacing: 0.3px; text-transform: uppercase; color: #3a3a3a;
  }
</style>
</head>
<body>
<main class="canvas">

  <section class="card card--front" aria-label="Business card front">
    <div class="front-mark" aria-hidden="true"></div>
    <p class="front-name">Marcus Delvaney</p>
    <p class="front-tagline">Designer Jewellery</p>
    <p class="front-country">Australia</p>
    <div class="front-ornament" role="img" aria-label="Silver foil scrollwork border ornament along the lower edge"></div>
  </section>

  <section class="card card--back" aria-label="Business card back">
    <div class="back-brand">
      <span class="back-brand__circle" aria-hidden="true"></span>
      <span class="back-brand__name">Marcus Delvaney</span>
    </div>
    <div class="back-divider"></div>
    <div class="back-identity">
      <h1 class="back-identity__name">Marcus Delvaney</h1>
      <p class="back-identity__role">Your Jewellery Stylist</p>
    </div>
    <ul class="contact-list">
      <li class="contact-list__item">
        <svg class="contact-list__icon" viewBox="0 0 12 12" aria-hidden="true">
          <rect x="3" y="0.5" width="6" height="11" rx="1" fill="#1a1a1a"/>
          <rect x="4" y="2" width="4" height="7" fill="#fff"/>
        </svg>
        <span>0492 836 514</span>
      </li>
      <li class="contact-list__item">
        <svg class="contact-list__icon" viewBox="0 0 12 12" aria-hidden="true">
          <rect x="0.5" y="2.5" width="11" height="7" fill="#1a1a1a"/>
          <path d="M0.5 2.5 L6 6.5 L11.5 2.5" fill="none" stroke="#fff" stroke-width="1"/>
        </svg>
        <span>marcus@marcusdelvaney.com</span>
      </li>
      <li class="contact-list__item">
        <svg class="contact-list__icon" viewBox="0 0 12 12" aria-hidden="true">
          <circle cx="6" cy="6" r="5.5" fill="#1a1a1a"/>
          <ellipse cx="6" cy="6" rx="2.3" ry="5.5" fill="none" stroke="#fff" stroke-width="0.8"/>
          <line x1="0.5" y1="6" x2="11.5" y2="6" stroke="#fff" stroke-width="0.8"/>
        </svg>
        <span>www.marcusdelvaney.com</span>
      </li>
    </ul>
    <div class="back-shadow" aria-hidden="true"></div>
    <p class="back-country">Australia</p>
  </section>

</main>
</body>
</html>
```